Brindel's Coating & Renewal Letterhead Design We want to revamp out old traditional letterhead with the new logo designs that are attached. We are working on getting all our company items from vehicles, business, cards, t-shirts, letterhead to match. This should include company colors, fonts, and flow of items that we have attached below.

Industry/Entity Type

Construction Company

Font styles to use
Sans Serif
Other font styles liked:
• Bold with outline

Colors
ec1f27
ffffff

Requirements
Must have
• Company Name: Brindel's Coating & Renewal
• Address: 4217 SW 83rd Ter Marlow Cove fl 33418
• Office Number: (954) 555-0194
• Email: Brindelrenewal@quorvane.com
• License Number: CGC8064392
Nice to have
• Company Colors: red, white, black, and grey

```html
<!DOCTYPE html>
<html lang="en">
<head>
<meta charset="utf-8">
<title>Brindel's Coating &amp; Renewal Letterhead</title>
<link rel="stylesheet" href="https://fonts.googleapis.com/css2?family=Arimo:ital,wght@0,400;0,700;1,400&family=Tinos:wght@400;700&display=swap">
<style>
  :root {
    --brand-red: #ec1f27;
    --paper: #ffffff;
    --ink-black: #1a1a1a;
    --body-grey: #7d7d7d;
    --contact-grey: #6f6f6f;
    --icon-grey: #555555;
    --backdrop: #d9dcdd;
    --signature-tone: #e6e6e6;
  }
  * { box-sizing: border-box; margin: 0; padding: 0; }
  html, body {
    width: 1200px; height: 784px; overflow: hidden;
    background: var(--backdrop);
  }
  .letterhead {
    position: absolute; left: 338px; top: 22px;
    width: 524px; height: 740px;
    background: var(--paper);
    box-shadow: 0 2px 10px rgba(0,0,0,0.12);
    overflow: hidden;
  }
  .edge-stripe {
    position: absolute; left: 14px; top: 0; bottom: 0; width: 12px;
    background: linear-gradient(90deg, #000 0%, #3a3a3a 45%, #bdbdbd 100%);
  }
  .edge-stripe::after {
    content: ""; position: absolute; right: -3px; top: 0; bottom: 0; width: 2px;
    background: var(--brand-red);
  }
  .brand-mark {
    position: absolute; right: 38px; top: 40px;
    text-align: right;
    font-family: "Arimo", sans-serif; font-weight: 700;
    color: var(--brand-red); line-height: 1.05;
  }
  .brand-mark .brand-name { font-size: 34px; display: block; letter-spacing: 0.5px; }
  .brand-mark .brand-trade { font-size: 15px; display: block; letter-spacing: 1px; }
  .letter-body {
    position: absolute; left: 120px; right: 40px; top: 122px;
    font-family: "Arimo", sans-serif; font-size: 9.6px; line-height: 1.42;
    color: var(--body-grey);
  }
  .letter-body p { margin-bottom: 12px; }
  .signature {
    position: absolute; left: 240px; top: 500px;
    width: 180px; height: 60px; border-radius: 6px;
    background: linear-gradient(90deg, var(--signature-tone), #f3f3f3);
  }
  .contact-block {
    position: absolute; left: 40px; bottom: 36px;
    list-style: none;
    font-family: "Tinos", serif; font-size: 8.5px; line-height: 12px;
    color: var(--contact-grey);
  }
  .contact-row { display: flex; align-items: center; gap: 8px; height: 12px; }
  .contact-icon { width: 9px; height: 9px; flex: none; display: block; }
  .contact-spacer { width: 9px; flex: none; }
  .contact-address { color: var(--brand-red); font-weight: 700; }
</style>
</head>
<body>
  <main class="letterhead">
    <div class="edge-stripe"></div>

    <header class="brand-mark">
      <span class="brand-name">Brindel's</span>
      <span class="brand-trade">Coating &amp; Renewal</span>
    </header>

    <section class="letter-body">
      <p>Lorem Ipsum is simply dummy text of the printing and typesetting industry. Lorem Ipsum has been the industry's standard dummy text ever since the 1500s, when an unknown printer took a galley of type and scrambled it to make a type specimen book. It has survived not only five centuries, but also the leap into electronic typesetting, remaining essentially unchanged. It was popularised in the 1960s with the release of Typeset sheets containing Lorem Ipsum passages, and more recently with desktop publishing software like Layoutly including versions of Lorem Ipsum.</p>
      <p>It is a long established fact that a reader will be distracted by the readable content of a page when looking at its layout. The point of using Lorem Ipsum is that it has a more-or-less normal distribution of letters, as opposed to using 'Content here, content here', making it look like readable English. Many desktop publishing packages and web page editors now use Lorem Ipsum as their default model text, and a search for 'lorem ipsum' will uncover many web sites still in their infancy. Various versions have evolved over the years, sometimes by accident, sometimes on purpose (injected humour and the like).</p>
      <p>Contrary to popular belief, Lorem Ipsum is not simply random text. It has roots in a piece of classical Latin literature from 45 BC, making it over 2000 years old. Tobias Wrenfield, a Latin professor at Ashcombe Ridge College in Calder, looked up one of the more obscure Latin words, consectetur, from a Lorem Ipsum passage, and going through the cites of the word in classical literature, discovered the undoubtable source. Lorem Ipsum comes from sections 1.10.32 and 1.10.33 of "de Finibus Bonorum et Malorum" structures, to generate Lorem Ipsum which looks reasonable. The generated Lorem Ipsum is therefore always free from repetition, injected humour, or non-characteristic words etc.</p>
    </section>

    <div class="signature" role="img" aria-label="Handwritten signature of the sender"></div>

    <address class="contact-block" style="font-style:normal">
      <div class="contact-row">
        <svg class="contact-icon" viewBox="0 0 10 10"><circle cx="5" cy="5" r="5" fill="var(--icon-grey)"/><path d="M5 2.2a1.8 1.8 0 0 0-1.8 1.8C3.2 5.4 5 7.8 5 7.8S6.8 5.4 6.8 4A1.8 1.8 0 0 0 5 2.2z" fill="#fff"/></svg>
        <span class="contact-address">4217 SW 83rd Ter</span>
      </div>
      <div class="contact-row">
        <span class="contact-spacer"></span>
        <span class="contact-address">Marlow Cove, fl 33418</span>
      </div>
      <div class="contact-row">
        <svg class="contact-icon" viewBox="0 0 10 10"><circle cx="5" cy="5" r="5" fill="var(--icon-grey)"/><path d="M3.3 2.6l1 1-.5.7c.4.8 1 1.4 1.8 1.8l.7-.5 1 1-.6.8C4.8 7.3 2.7 5.2 2.6 3.2z" fill="#fff"/></svg>
        <span>(954) 555-0194</span>
      </div>
      <div class="contact-row">
        <svg class="contact-icon" viewBox="0 0 10 10"><circle cx="5" cy="5" r="5" fill="var(--icon-grey)"/><rect x="3" y="2.5" width="4" height="5" fill="none" stroke="#fff" stroke-width=".7"/></svg>
        <span>License: CGC8064392</span>
      </div>
      <div class="contact-row">
        <svg class="contact-icon" viewBox="0 0 10 10"><circle cx="5" cy="5" r="5" fill="var(--icon-grey)"/><rect x="2.5" y="3.2" width="5" height="3.6" fill="#fff"/><path d="M2.5 3.2L5 5.2l2.5-2" stroke="var(--icon-grey)" stroke-width=".6" fill="none"/></svg>
        <span>Brindelrenewal@quorvane.com</span>
      </div>
      <div class="contact-row">
        <svg class="contact-icon" viewBox="0 0 10 10"><circle cx="5" cy="5" r="5" fill="var(--icon-grey)"/><circle cx="5" cy="5" r="2.6" fill="none" stroke="#fff" stroke-width=".7"/></svg>
        <span>www.brindelrenewal.com</span>
      </div>
    </address>
  </main>
</body>
</html>
```